Game, Voice & Dedicated Server Company Needs a Business Card Design

We need a new business card design, centered around our new logo (PSD provided below).

Designs that we do like:
https://plomvaste.net/item/corporate-business-card/5382047?s_rank=31 (needs to be made more eye catching)

Our main areas of business are:
- Dedicated Servers
- Game Servers
- Voice Servers
- Mitigation Security Specialists

Industry/Entity Type

Business

Contact Information for Business Card

On the card: (and anything else you would suggest)
- Staff member name
- Staff member position in company
- Staff member phone number
- Staff member email
- Other / Staff member Skype
- Website link

Colors
9bcb3c
abd036

Requirements
Must have
• Design of Card:
• - Green (same green as the logo)
• - Business / Corporate design
• - Something a little different / abstract that shouts premium

```html
<!DOCTYPE html>
<html lang="en">
<head>
<meta charset="utf-8">
<title>Brightpath Hosting – Business Card</title>
<link rel="stylesheet" href="https://fonts.googleapis.com/css2?family=Open+Sans:ital,wght@0,400;0,600;0,700;1,400&display=swap">
<style>
  :root {
    --green: #8dc63f;
    --green-light: #a4d254;
    --green-dark: #6fa82e;
    --black: #111213;
    --black-soft: #2a2c2e;
    --white: #ffffff;
    --ink: #1d2a10;
    --grey-text: #2b2b2b;
    --page: #e9eae6;
  }
  * { box-sizing: border-box; margin: 0; padding: 0; }
  html, body { width: 1200px; height: 950px; overflow: hidden; }
  body {
    background: var(--page);
    font-family: "Open Sans", Arial, sans-serif;
    display: flex;
    flex-direction: column;
    align-items: center;
    justify-content: center;
    gap: 40px;
  }
  .card {
    position: relative;
    width: 700px;
    height: 400px;
    overflow: hidden;
    box-shadow: 0 6px 18px rgba(0,0,0,0.18);
  }
  .card-front { background: var(--green); }
  .card-front .shapes { position: absolute; inset: 0; width: 100%; height: 100%; }

  .brand {
    position: absolute;
    display: flex;
    align-items: center;
    gap: 12px;
  }
  .brand-mark { width: 22px; height: 22px; background: var(--green); flex: none; }
  .brand-name {
    font-weight: 700;
    letter-spacing: 1px;
    text-transform: uppercase;
    line-height: 1.05;
  }
  .card-front .brand { top: 70px; left: 340px; width: 260px; }
  .card-front .brand-name { color: var(--white); font-size: 30px; }

  .person { position: absolute; left: 34px; top: 248px; }
  .person-name { font-size: 21px; font-weight: 600; color: var(--ink); letter-spacing: 0.5px; }
  .person-role { font-size: 14px; color: var(--ink); margin-top: 2px; }

  .contacts {
    position: absolute;
    left: 290px;
    top: 290px;
    list-style: none;
    font-size: 14px;
    color: var(--grey-text);
  }
  .contacts li { display: flex; align-items: center; gap: 10px; height: 23px; }
  .contacts svg { width: 14px; height: 14px; fill: var(--black); flex: none; }

  .card-back { background: var(--white); }
  .card-back .brand {
    top: 140px;
    left: 0;
    right: 0;
    justify-content: center;
    gap: 18px;
  }
  .card-back .brand-mark { width: 40px; height: 40px; }
  .card-back .brand-name { color: var(--green-dark); font-size: 46px; }
  .services {
    position: absolute;
    left: 0; right: 0; bottom: 48px;
    display: flex;
    justify-content: center;
    gap: 22px;
    list-style: none;
    font-size: 15px;
    font-style: italic;
    color: var(--grey-text);
  }
  .services li { display: flex; align-items: center; gap: 8px; }
  .services li::before {
    content: "";
    width: 7px; height: 7px; border-radius: 50%;
    background: var(--green);
  }
</style>
</head>
<body>

  <section class="card card-front" aria-label="Business card front">
    <svg class="shapes" viewBox="0 0 700 400" preserveAspectRatio="none" aria-hidden="true">
      <polygon points="0,0 120,0 70,400 0,400" fill="var(--green-light)" opacity="0.6"/>
      <polygon points="215,310 700,120 700,400 140,400" fill="var(--green-light)"/>
      <polygon points="170,0 700,0 700,120 215,310" fill="var(--black)"/>
      <polygon points="170,0 700,0 700,55 195,190" fill="var(--black-soft)" opacity="0.45"/>
    </svg>

    <div class="brand">
      <span class="brand-mark"></span>
      <span class="brand-name">Brightpath Hosting</span>
    </div>

    <div class="person">
      <p class="person-name">MARCUS HALE</p>
      <p class="person-role">CEO/Founder</p>
    </div>

    <ul class="contacts">
      <li>
        <svg viewBox="0 0 24 24"><path d="M6.6 10.8a15.1 15.1 0 0 0 6.6 6.6l2.2-2.2a1 1 0 0 1 1-.25 11.4 11.4 0 0 0 3.6.57 1 1 0 0 1 1 1V20a1 1 0 0 1-1 1A17 17 0 0 1 3 4a1 1 0 0 1 1-1h3.5a1 1 0 0 1 1 1c0 1.25.2 2.45.57 3.6a1 1 0 0 1-.25 1z"/></svg>
        604 218 7731
      </li>
      <li>
        <svg viewBox="0 0 24 24"><path d="M2 5h20v14H2z M4 7v.5l8 5 8-5V7l-8 5z" fill-rule="evenodd"/></svg>
        name@brightpath.com
      </li>
      <li>
        <svg viewBox="0 0 24 24"><circle cx="12" cy="12" r="10"/></svg>
        www.brightpath.com
      </li>
      <li>
        <svg viewBox="0 0 24 24"><circle cx="12" cy="12" r="10"/></svg>
        brightpath.com
      </li>
    </ul>
  </section>

  <section class="card card-back" aria-label="Business card back">
    <div class="brand">
      <span class="brand-mark"></span>
      <span class="brand-name">Brightpath</span>
    </div>
    <ul class="services">
      <li>Dedicated Servers</li>
      <li>Game Servers</li>
      <li>Voice Servers</li>
      <li>Business relations</li>
    </ul>
  </section>

</body>
</html>
```